Trvmlegal.com needs a wedsite. Law Office of Darnell P. Whitby

Darnell P. Whitby is a criminal law firm that is 5 years old. We have already had all the content written and now just need the website designed. We also just finished our logo design using Pixel Harbor and would like it used in the design of the website.

Industry/Entity Type

Law Firm

Number of Pages Required

5+ page

Requirements
Must have
• I was our new logo to be on the website also. I want Dallas sites as the stock pictures for the website. For example the Grey Stone Tribunal. I also need to be able to add YouTube videos. It has to adjust to be seen on computers and also cell phones. I need to be able to have a information sheet for clients to fill out and submit back to me.

```html
<!DOCTYPE html>
<html lang="en">
<head>
<meta charset="utf-8">
<title>Law Office of Darnell P. Whitby</title>
<link rel="stylesheet" href="https://fonts.googleapis.com/css2?family=Merriweather:ital,wght@0,300;0,400;1,300&family=Open+Sans:ital,wght@0,400;0,600;1,400&display=swap">
<style>
:root{
  --navy:#12288a;
  --navy-deep:#0b1a63;
  --band:#1a34a8;
  --ink:#222;
  --body:#444;
  --white:#fff;
  --footer:#0d0d0d;
  --footer-bar:#161616;
  --footer-text:#8a8a8a;
}
*{margin:0;padding:0;box-sizing:border-box}
html,body{width:738px;height:1200px;overflow:hidden;background:var(--white)}
body{position:relative;font-family:"Open Sans",sans-serif;color:var(--body)}
.abs{position:absolute}

/* hero */
.hero{left:0;top:0;width:738px;height:348px;background:linear-gradient(90deg,#3a2a22 0%,#5a4132 25%,#2c2a2c 48%,#3a3f48 70%,#2a2e36 100%)}
.nav{left:0;top:50px;width:738px;height:32px;background:linear-gradient(#1c3bb8,#0f248c)}
.nav a{position:absolute;top:10px;font-family:"Merriweather",serif;font-size:8.5px;color:var(--white);text-decoration:none;letter-spacing:.3px;text-transform:uppercase;white-space:nowrap}
.brand{left:315px;top:12px;width:108px;height:108px;border-radius:50%;background:var(--navy);border:3px solid var(--white);box-shadow:0 0 0 2px var(--navy);display:flex;align-items:center;justify-content:center;text-align:center}
.brand span{font-family:"Merriweather",serif;font-size:10.5px;line-height:1.35;color:var(--white);width:80px}
.hero-title{left:37px;top:132px;font-family:"Merriweather",serif;font-weight:400;font-size:37px;line-height:46px;color:var(--white);text-shadow:0 2px 4px rgba(0,0,0,.4);white-space:nowrap}
.hero-sub{left:37px;top:184px;font-family:"Merriweather",serif;font-weight:300;font-size:15px;line-height:20px;color:var(--white);white-space:nowrap}
.hero-lead{left:37px;top:216px;font-size:8px;line-height:10.5px;color:var(--white);width:200px}
.btn{position:absolute;background:var(--navy);color:var(--white);font-size:9.5px;text-align:center;border-radius:2px;white-space:nowrap}
.dots{left:341px;top:327px;line-height:0}
.dots i{display:inline-block;width:15px;height:2px;background:var(--white);margin-right:5px}
.dots i:first-child{background:#2a5cff}

/* practice band */
.band{left:0;top:348px;width:738px;height:250px;background:linear-gradient(#15309e,#1e3aac 70%,#0f2480)}
.card{top:375px;width:209px;height:190px;background:linear-gradient(#fff 70%,#eef0f6);box-shadow:0 10px 14px rgba(0,0,20,.35);text-align:center}
.card .icon{position:absolute;left:71px;top:10px;width:66px;height:66px;border-radius:50%;background:var(--navy)}
.card h3{position:absolute;left:0;top:82px;width:100%;font-family:"Merriweather",serif;font-weight:300;font-size:14px;color:var(--ink);white-space:nowrap}
.card p{position:absolute;left:14px;top:104px;width:181px;font-size:8px;line-height:13.5px;color:var(--body)}
.card .btn{left:71px;top:155px;width:70px;height:21px;line-height:21px}
.arrow{top:459px}

/* welcome */
.welcome-title{left:0;top:616px;width:738px;text-align:center;font-family:"Merriweather",serif;font-weight:300;font-size:22px;color:var(--ink)}
.welcome-title em{font-style:normal;color:var(--navy)}
.welcome-tag{left:0;top:652px;width:738px;text-align:center;font-size:9px;font-style:italic;color:var(--navy)}
.welcome-text{left:42px;top:673px;width:654px;text-align:center;font-size:8px;line-height:13.5px;color:var(--body)}

/* attorneys */
.team-title{left:35px;top:773px;font-family:"Merriweather",serif;font-weight:300;font-size:22px;color:var(--ink)}
.team-title em{font-style:normal;color:var(--navy)}
.person{width:215px;height:101px}
.person .photo{position:absolute;left:0;top:0;width:81px;height:101px;background:linear-gradient(#cfcfcf,#5c5c5c)}
.person h4{position:absolute;left:88px;top:-3px;white-space:nowrap;font-family:"Merriweather",serif;font-weight:400;font-size:11px;color:var(--navy)}
.person p{position:absolute;left:90px;top:17px;width:125px;font-size:7.6px;line-height:13.6px;color:var(--body)}
.person .more{position:absolute;left:91px;top:91px;font-size:7.6px;color:var(--navy);white-space:nowrap}

/* footer */
.footer{left:0;top:980px;width:738px;height:178px;background:var(--footer)}
.footbar{left:0;top:1158px;width:738px;height:42px;background:var(--footer-bar)}
.fh{top:998px;font-family:"Merriweather",serif;font-weight:300;font-size:14px;color:var(--white);white-space:nowrap}
.flist{font-size:7px;line-height:17px;color:var(--footer-text);white-space:nowrap}
.contact{font-size:7.2px;line-height:11px;color:var(--white)}
.field{background:#0a0a0a;border:1px solid #2c2c2c;font-size:6.5px;color:#aaa;padding:6px 5px}
.social{top:1166px;width:19px;height:19px;border:1px solid #3a3a3a}
.copy{left:37px;top:1173px;font-size:8px;color:#9a9a9a;white-space:nowrap}
</style>
</head>
<body>

<section class="hero abs" role="img" aria-label="Photo of an attorney in a dark suit with arms folded before a law library bookshelf"></section>
<nav class="nav abs">
  <a style="left:37px">Home</a>
  <a style="left:98px">Our Attorneys</a>
  <a style="left:202px">Practice Areas</a>
  <a style="left:450px">Why We Are Different</a>
  <a style="left:591px">Contact Us</a>
  <a style="left:689px">Blog</a>
</nav>
<div class="brand abs"><span>Darnell P. Whitby</span></div>
<h1 class="hero-title abs">Expertise</h1>
<div class="hero-sub abs">in a criminal law</div>
<p class="hero-lead abs">We have found that approaching our client's cases with this perspective ways the foundation</p>
<div class="btn" style="left:37px;top:253px;width:71px;height:29px;line-height:29px">Read More</div>
<div class="dots abs"><i></i><i></i><i></i></div>

<section class="band abs"></section>
<svg class="arrow abs" style="left:19px" width="12" height="16" viewBox="0 0 12 16"><path d="M9 2 3 8l6 6" fill="none" stroke="#fff" stroke-width="2.6"/></svg>
<svg class="arrow abs" style="left:707px" width="12" height="16" viewBox="0 0 12 16"><path d="M3 2l6 6-6 6" fill="none" stroke="#fff" stroke-width="2.6"/></svg>

<article class="card abs" style="left:36px">
  <div class="icon" role="img" aria-label="Knife icon"></div>
  <h3>Murder &amp; Other Homicide</h3>
  <p>Our attorneys are knowledgeable about DNA, ballistic, fingerprint, fiber analysis and other scientific evidence to defend</p>
  <div class="btn">Read More</div>
</article>
<article class="card abs" style="left:265px">
  <div class="icon" role="img" aria-label="Two people icon"></div>
  <h3>Sexual Offenses</h3>
  <p>We defend you against serious charges including rape, child pornography and sex assault, and we fight against your inclusion</p>
  <div class="btn">Read More</div>
</article>
<article class="card abs" style="left:493px">
  <div class="icon" role="img" aria-label="Police officer icon"></div>
  <h3>Probation Violations</h3>
  <p>Our lawyers help you make a fresh start through criminal record expungement and non-disclosure.</p>
  <div class="btn">Read More</div>
</article>

<section class="welcome">
  <h2 class="welcome-title abs">Welcome to <em>Darnell P. Whitby</em></h2>
  <div class="welcome-tag abs">Dallas Defense Law Firm Advocates for Your Rights</div>
  <p class="welcome-text abs">The Law Office of Darnell P. Whitby was founded on the principle embedded in the U.S. Constitution, which states not only that all men are created equal, but that everyone is innocent until proven guilty. Yet, we recognize the criminal process often slants toward the prosecution of individuals instead of the pursuit of justice. Our goal is to balance the scales through zealous advocacy.</p>
  <div class="btn" style="left:334px;top:728px;width:70px;height:26px;line-height:26px">Read More</div>
</section>

<h2 class="team-title abs">Our &nbsp;<em>Attorney</em></h2>

<div class="person abs" style="left:37px;top:829px">
  <div class="photo" role="img" aria-label="Portrait of Darnell P. Whitby"></div>
  <h4>Darnell P. Whitby</h4>
  <p>Darnell P. Whitby is the managing partner of our law firm. Before founding his own practice, he worked for one of the best criminal defense law firms...</p>
  <div class="more">Read More &#9656;</div>
</div>
<div class="person abs" style="left:265px;top:829px">
  <div class="photo" role="img" aria-label="Portrait of Renata Oakes-Malloy"></div>
  <h4>Renata Oakes-Malloy</h4>
  <p>Darnell P. Whitby is the managing partner of our law firm. Before founding his own practice, he worked for one of the best criminal defense law firms...</p>
  <div class="more">Read More &#9656;</div>
</div>
<div class="person abs" style="left:493px;top:829px">
  <div class="photo" role="img" aria-label="Portrait of Tobin Ashcraft"></div>
  <h4>Tobin Ashcraft</h4>
  <p>Darnell P. Whitby is the managing partner of our law firm. Before founding his own practice, he worked for one of the best criminal defense law firms...</p>
  <div class="more">Read More &#9656;</div>
</div>

<footer>
  <div class="footer abs"></div>
  <h5 class="fh abs" style="left:37px">Contact us</h5>
  <h5 class="fh abs" style="left:175px">Areas of Practice</h5>
  <h5 class="fh abs" style="left:447px">Company</h5>
  <h5 class="fh abs" style="left:541px">Contact Form</h5>

  <svg class="abs" style="left:37px;top:1032px" width="8" height="11" viewBox="0 0 8 11"><path d="M4 0a4 4 0 0 0-4 4c0 3 4 7 4 7s4-4 4-7a4 4 0 0 0-4-4z" fill="#bbb"/><circle cx="4" cy="4" r="1.5" fill="#0d0d0d"/></svg>
  <div class="contact abs" style="left:51px;top:1032px;width:90px">Nemo enim ipsam voluptatem quia voluptas sit aspernatur aut odit</div>
  <svg class="abs" style="left:38px;top:1093px" width="6" height="10" viewBox="0 0 6 10"><rect x=".5" y=".5" width="5" height="9" rx="1" fill="none" stroke="#bbb"/></svg>
  <div class="contact abs" style="left:51px;top:1094px">1800-555-014</div>
  <svg class="abs" style="left:37px;top:1116px" width="9" height="7" viewBox="0 0 9 7"><rect width="9" height="7" fill="#bbb"/><path d="M0 0l4.5 3.5L9 0" fill="none" stroke="#0d0d0d"/></svg>
  <div class="contact abs" style="left:52px;top:1113px">hello@trvmlegal.net</div>

  <div class="flist abs" style="left:175px;top:1030px">Murder &amp; Other Homicide Offenses<br>Sexual Offenses<br>Expungements &amp; Non-Disclosures<br>Early Probation Release</div>
  <div class="flist abs" style="left:330px;top:1033px">Probation Violations<br>Other Violent Offenses<br>DWI, DUI<br>Drug Offenses</div>
  <div class="flist abs" style="left:449px;top:1033px">Services Provided<br>Contact Us<br>How To Find Us</div>

  <div class="field abs" style="left:541px;top:1038px;width:159px;height:21px">Mail Address</div>
  <div class="field abs" style="left:541px;top:1066px;width:159px;height:57px">Message</div>
  <div class="btn" style="left:541px;top:1131px;width:43px;height:17px;line-height:17px;font-size:9px;background:var(--band)">Submit</div>

  <div class="footbar abs"></div>
  <div class="copy abs">© 2015 trvmlegal.net. All right Reserved.</div>
  <div class="social abs" style="left:599px"></div>
  <div class="social abs" style="left:621px"></div>
  <div class="social abs" style="left:643px"></div>
  <div class="social abs" style="left:665px"></div>
  <div class="social abs" style="left:687px"></div>
</footer>

</body>
</html>
```